Marketing Skill "Workouts"; Design for an e-mail attachment highlighting Marketing training subjects

I am a freelance marketing trainer based in Singapore and need to e-mail out an attachment (probably saved as a PDF) to potential clients showing the training services I offer. These clients are all large blue-chip multinational companies so the attachment needs to look professional/high quality when opened on a computer.

My Company is called "Clearpath Marketing" (logo attached)

I am assuming the size should be A4 one sided colour.

I have attached some files that show best-attempts so far. These contain the key information, but the layouts all still look rather pedestrian. I am looking for something that looks a bit more dynamic but remains clear/easy to read.

Target Market(s)

HR/Marketing managers in multinational firms, mainly consumer goods

Industry/Entity Type

Marketing

Font styles to use
Sans Serif

Colors

Designer to choose colors to be used in the design.

Requirements
Must have
• Must look modern, up-to-date, professional.
Should not have
• Not gimmicky, like a cheap deal

```html
<!DOCTYPE html>
<html lang="en">
<head>
<meta charset="utf-8">
<title>Marketing skill Workouts – Clearpath Marketing</title>
<link rel="stylesheet" href="https://fonts.googleapis.com/css2?family=Questrial&family=Mukta:wght@500;600;700&display=swap">
<style>
  :root{
    --backdrop:#58595b;
    --sheet:#9c9c9c;
    --sheet-dark:#858585;
    --red:#c21f30;
    --red-deep:#9a1622;
    --teal:#245b6b;
    --white:#ffffff;
    --ink:#151515;
    --panel-band:rgba(110,110,110,.85);
  }
  *{box-sizing:border-box;margin:0;padding:0}
  html,body{width:1200px;height:1000px;overflow:hidden;background:var(--backdrop)}
  body{font-family:"Mukta",sans-serif;color:var(--ink)}
  .canvas{position:relative;width:1200px;height:1000px}
  .shapes{position:absolute;inset:0}
  .abs{position:absolute}

  .title-light{left:132px;top:176px;font-family:"Questrial",sans-serif;font-size:47px;color:var(--white);letter-spacing:.5px;line-height:1.1}
  .title-bold{left:130px;top:228px;font-weight:700;font-size:46px;color:var(--red);line-height:1.1}
  .intro{left:134px;top:307px;width:400px;font-size:14.5px;font-weight:600;line-height:18px;color:var(--white)}

  .banner-title{color:var(--white);font-weight:600;line-height:1}
  .topics-title{left:218px;top:422px;font-size:27px}
  .benefits-title{left:559px;top:438px;font-size:27px}

  .topic-list{left:172px;top:478px;width:225px;list-style:none;font-size:12.6px;font-weight:600;line-height:15.5px}
  .topic-list li{position:relative;padding-left:16px;margin-bottom:6px}
  .topic-list li::before{content:"";position:absolute;left:2px;top:5px;width:5px;height:5px;border-radius:50%;background:var(--red)}
  .topic-list li.plain::before{display:none}

  .benefit{left:497px;font-size:12.6px;font-weight:600;line-height:15.5px;padding-left:18px;width:200px}
  .benefit::before{content:"";position:absolute;left:1px;top:5px;width:6px;height:6px;border-radius:50%;background:var(--red-deep)}

  .why-heading{left:857px;top:498px;font-size:29px;font-weight:700;color:var(--ink);line-height:1}
  .why-body{left:856px;top:538px;width:200px;font-size:14.5px;font-weight:500;line-height:18px;color:var(--white)}
  .why-body strong{color:var(--ink);font-weight:600;font-size:16px}

  .keep{left:126px;top:780px;font-size:37px;font-weight:700;color:var(--red);line-height:1}
  .contact{left:540px;font-size:16px;font-weight:600;color:var(--white);line-height:1}
  .brand{left:876px;top:808px;font-family:"Questrial",sans-serif;font-size:26px;color:var(--ink);line-height:1}
</style>
</head>
<body>
<div class="canvas">
  <svg class="shapes" width="1200" height="1000" viewBox="0 0 1500 1250" xmlns="http://www.w3.org/2000/svg">
    <defs>
      <linearGradient id="gymTones" x1="0" y1="0" x2="0" y2="1">
        <stop offset="0" stop-color="#34486a"/>
        <stop offset=".45" stop-color="#3f5a78"/>
        <stop offset=".75" stop-color="#6b6760"/>
        <stop offset="1" stop-color="#b38a5c"/>
      </linearGradient>
      <radialGradient id="sheetTone" cx=".4" cy=".4" r=".8">
        <stop offset="0" stop-color="#a3a3a3"/>
        <stop offset="1" stop-color="#939393"/>
      </radialGradient>
    </defs>

    <!-- sheet -->
    <rect x="118" y="183" width="1279" height="884" fill="url(#sheetTone)"/>

    <!-- hero photo area -->
    <polygon points="683,183 1397,183 1397,538 1018,538" fill="url(#gymTones)" role="img" aria-label="Photo of a man bench-pressing a barbell in a gym"/>
    <polyline points="655,183 1010,550 1397,550" fill="none" stroke="var(--red-deep)" stroke-width="3"/>

    <!-- intro band -->
    <rect x="118" y="376" width="555" height="86" fill="var(--panel-band)"/>

    <!-- key topics -->
    <rect x="201" y="578" width="299" height="338" fill="var(--white)" stroke="#c9c9c9"/>
    <path d="M200 510 H517 V580 H200 Z" fill="var(--red)"/>
    <path d="M500 580 H517 L500 590 Z" fill="var(--red-deep)"/>
    <circle cx="200" cy="545" r="50" fill="var(--red)"/>
    <circle cx="200" cy="545" r="38" fill="var(--white)"/>

    <!-- key benefits -->
    <rect x="609" y="614" width="298" height="302" fill="var(--white)" stroke="#c9c9c9"/>
    <path d="M625 512 H922 V620 H625 Z" fill="var(--red)"/>
    <path d="M907 620 H922 L907 628 Z" fill="var(--red-deep)"/>
    <circle cx="625" cy="565" r="60" fill="var(--red)"/>
    <circle cx="625" cy="565" r="46" fill="var(--white)"/>

    <!-- benefit icons -->
    <g fill="none" stroke="var(--red-deep)" stroke-width="2">
      <rect x="867" y="642" width="27" height="27"/>
      <path d="M873 664 V656 M879 664 V652 M885 664 V648 M890 664 V655"/>
      <rect x="867" y="713" width="27" height="19" rx="2"/>
      <path d="M875 713 V708 H886 V713 M867 721 H894"/>
      <circle cx="880" cy="773" r="10"/>
      <path d="M870 773 H890 M880 763 V783 M873 766 H887 M873 780 H887 M880 783 V790 M874 790 H886"/>
      <rect x="869" y="820" width="20" height="22"/>
      <path d="M873 817 V823 M879 817 V823 M885 817 V823 M873 830 H883 M873 836 H881 M886 840 L894 820"/>
      <circle cx="881" cy="884" r="12"/>
      <path d="M875 884 L880 889 L888 878"/>
    </g>

    <!-- why me frame -->
    <g stroke="var(--ink)" stroke-width="3" fill="none">
      <path d="M1070 605 H1337 V870"/>
      <path d="M1040 630 V898 H1305"/>
    </g>
    <text x="1016" y="660" font-family="Mukta, sans-serif" font-weight="700" font-size="110" fill="var(--ink)">“</text>
    <text x="1306" y="962" font-family="Mukta, sans-serif" font-weight="700" font-size="110" fill="var(--ink)">”</text>

    <!-- footer -->
    <rect x="118" y="957" width="1279" height="110" fill="var(--white)"/>
    <polygon points="517,957 1003,957 1055,1067 550,1067" fill="var(--teal)"/>
    <rect x="118" y="1050" width="432" height="17" fill="var(--teal)"/>

    <!-- phone icon -->
    <path d="M622 982 q-6 6 4 16 q10 10 16 4 l-5 -6 -4 2 q-4 -2 -7 -7 l2 -4 z" fill="var(--white)"/>
    <!-- mail icon -->
    <g fill="none" stroke="var(--white)" stroke-width="2">
      <rect x="619" y="1023" width="24" height="16"/>
      <path d="M619 1023 L631 1033 L643 1023"/>
    </g>

    <!-- brand mark -->
    <circle cx="1305" cy="1012" r="46" fill="var(--red-deep)"/>
  </svg>

  <div class="abs title-light">Marketing skill</div>
  <div class="abs title-bold">“Workouts”</div>
  <p class="abs intro">No time to learn? Problem solved with 1 day intensive workshops that will drive business growth and motivate your team</p>

  <h2 class="abs banner-title topics-title">Key Topics</h2>
  <ul class="abs topic-list">
    <li>Developing Strong Brand Plans</li>
    <li>Writing inspiring Briefs/Creative Evaluation</li>
    <li>Shopper Marketing/Developing Retail Promotions</li>
    <li>Brilliant Launch Management</li>
    <li class="plain">Improving Marketing R.O.I.</li>
    <li>Driving Brand Growth without Product Innovation</li>
    <li>Insight/Concept Development</li>
    <li>Integrating Digital Channels</li>
    <li>Creativity and Idea Generation</li>
  </ul>

  <h2 class="abs banner-title benefits-title">Key Benefits</h2>
  <div class="abs benefit" style="top:507px">Latest in world-class thinking/tools/case studies</div>
  <div class="abs benefit" style="top:551px">Ability to 'customise' to address your specific business issue</div>
  <div class="abs benefit" style="top:613px">Asian context/relevance</div>
  <div class="abs benefit" style="top:639px">Take-away 'checklists' to embed behaviours and skills</div>
  <div class="abs benefit" style="top:698px">Proven quality</div>

  <h2 class="abs why-heading">Why Me?</h2>
  <p class="abs why-body">The latest thinking, made practical and actionable. <strong>20 years</strong> of business experience combined with over 10 years of proven training/facilitation for major “blue-chip” clients, regularly scoring <strong>90%+ satisfaction</strong></p>

  <div class="abs keep">Keep in touch</div>
  <div class="abs contact" style="top:788px">+65 9000 4127</div>
  <div class="abs contact" style="top:818px">hello@clearpath-marketing.com</div>
  <div class="abs brand">Clearpath</div>
</div>
</body>
</html>
```